Donations Website - Fund page design

We need an on brand fund page for our crowdfunding website. The design should keep in mind Pinwheel Gridkit 3 default columns and spacing.

Please use this development site as a guide... ( under construction )
http://lerin.fundquay.example:8080/

Elements to include:
• Gridkit 3 default column layout ( based on 12 column / 1140px / 30px gutters )
• Fund title ( Default Page Fund Title )
• Fund image / video ( 16:9 ratio )
• Fund progress: Current $ amount, Goal $ amount, # donations, # supporters, # views, % progress, progress bar, # shares
• Share buttons ( Chatterly, Quillet, Orbix+, WorkNest, Clipsy, Email )
• Donate button
• Sections for ( Fund story, fund updates and fund comments... could be tabbed )
• Section for recent donations (name + ch photo / icon + anonymous / donation amount, short message )
• Button to report this fund
• Fund created by section ( name, chatterly photo if they've verified using chatterly and number of friends )
• Contact fund raiser button/link
Updates

The design brief has been updated. I've attached the logo as well, please use unless you feel you have something better to include.

Thanks.

I can't stress enough that this is 'NOT' a home page design. This is a personal fund page for a single user. Please do not include 'Other funds' on this page to promote.

Thanks,

Halvar

The page should be similar to these pages. As you can see, these are single fund pages within these sites. I do not want my page to look like these, but have the features I included in the brief while fitting my site's design.

http://www.pledgora.example/4kq9zm
https://www.backfolio.example/projects/512097734/lumo-rim?ref=home_location
http://www.raiseport.example/projects/the-river-hollows

Thanks,

Halvar

Target Market(s)

Adults age 18-50 mainly. Anyone that potentially needs to raise money.

Industry/Entity Type

Construction

Font styles to use
Sans Serif

Colors

Designer to choose colors to be used in the design.

Requirements
Must have
• • Gridkit 3 default column layout ( based on 12 column / 1140px / 30px gutters )
• Donate button
Nice to have
• Would be nice to keep in mind that users may be able to choose a theme color during fund setup. But if the design is strong enough on its own we will not include this option.

```html
<!DOCTYPE html>
<html lang="en">
<head>
<meta charset="utf-8">
<title>Default Page Fund Title – Fundquay</title>
<link rel="stylesheet" href="https://fonts.googleapis.com/css2?family=Titillium+Web:wght@300;400;600;700&display=swap">
<style>
:root{
  --accent-blue:#1e8fe6;
  --red:#e84c3d;
  --dark:#3b4249;
  --green:#5bb12f;
  --text:#3a3a3a;
  --muted:#9a9a9a;
  --page:#f5f5f5;
  --panel:#efefef;
  --line:#dcdcdc;
  --white:#ffffff;
  --footer:#2c2e2c;
  --footer-link:#e7ecd9;
}
*{box-sizing:border-box;margin:0;padding:0}
html,body{width:688px;height:1200px;overflow:hidden}
body{position:relative;background:var(--page);font-family:'Titillium Web',sans-serif;color:var(--text)}
.abs{position:absolute}
.topbar{left:0;top:0;width:688px;height:4px;background:var(--accent-blue)}
.header{left:0;top:4px;width:688px;height:47px;background:var(--white);border-bottom:1px solid #e6e6e6}
.brand{left:77px;top:19px;display:flex;align-items:center;gap:4px;font-weight:700;font-size:9px;letter-spacing:1px;color:#6b6f72;text-transform:uppercase}
.brand-dot{width:9px;height:9px;border-radius:50%;background:#6b6f72}
.nav{top:21px;font-size:7.5px;color:#444;text-transform:uppercase}
.nav.active{color:var(--red)}
.nav-sep{top:20px;height:12px;border-left:1px dotted #ccc}
.btn{display:flex;align-items:center;justify-content:center;color:#fff;border-radius:2px;font-size:7.5px}
.btn-red{background:var(--red)}
.btn-dark{background:var(--dark)}
.fund-title{left:76px;top:70px;font-size:15px;font-weight:600;color:#333}
.fund-by{left:76px;top:96px;font-size:7px;color:var(--muted);font-weight:600}
.card{background:var(--white);border:1px solid var(--line)}
.card-grey{background:var(--panel);border:1px solid var(--line)}
.media{border:1px solid var(--line);padding:2px;background:#fff}
.media-fill{width:100%;height:100%}
.stat-label{font-size:6px;color:var(--muted);letter-spacing:.3px}
.stat-value{font-size:10px;font-weight:600;color:#333}
.stat-sep{top:418px;height:20px;border-left:1px dotted #ccc}
.tab{top:469px;height:20px;font-size:7px;display:flex;align-items:center;justify-content:center;color:#555}
.tab.active{background:#fff;border:1px solid var(--line);border-bottom:none;color:var(--red)}
.story-h{left:91px;top:504px;font-size:10.5px;color:#333}
.story-by{left:91px;top:522px;font-size:6.5px;color:#bbb}
.para{left:91px;width:320px;font-size:6.6px;line-height:12px;color:#555}
.caption{left:91px;top:849px;font-size:6.5px;color:#bbb}
.share{display:flex;gap:6px;align-items:center}
.share-btn{display:flex;align-items:center;height:11px;font-size:5.6px}
.share-btn .lbl{border:1px solid #c9c9c9;background:#f4f4f4;padding:0 3px;height:11px;display:flex;align-items:center;gap:2px;color:#333;font-weight:600}
.share-btn .sq{width:5px;height:5px;background:#4a6ea9}
.share-btn .sq.q{background:#3aa5dc}
.share-btn .sq.o{background:var(--red)}
.share-btn .cnt{border:1px solid #c9c9c9;background:#fff;padding:0 3px;height:11px;display:flex;align-items:center;margin-left:3px;color:#555}
.side-small{font-size:6.8px;font-weight:600;color:#333}
.side-title{font-size:9px;font-weight:600;color:#333;letter-spacing:.2px}
.donate{left:452px;top:178px;width:151px;height:44px;background:var(--green);border-radius:2px;color:#fff;text-align:center}
.donate b{display:block;margin-top:8px;font-size:9.5px;font-weight:600}
.donate span{display:block;font-size:6.5px;color:#d8f0c8;margin-top:2px}
.recent-title{left:453px;top:453px;font-size:10px;color:#444}
.divider{left:453px;width:146px;border-top:1px solid var(--line)}
.don-amount{left:454px;font-size:12.5px;color:var(--green)}
.don-time{left:552px;width:46px;text-align:right;font-size:6px;color:#bbb}
.avatar{left:453px;width:32px;height:32px;border-radius:50%;background:#fff;border:1px solid #e0e0e0}
.avatar.photo{background:linear-gradient(135deg,#7d6a5a,#3c3a3c)}
.don-name{left:490px;font-size:8px;color:#444}
.don-msg{left:490px;font-size:6.4px;line-height:11px;color:#555;width:120px}
.footer{left:0;top:1072px;width:688px;height:128px;background:var(--footer);border-top:4px solid #fff}
.f-head{top:1089px;font-size:9.5px;color:#fff}
.f-links{top:1110px;font-size:7px;line-height:11.5px;color:var(--footer-link);list-style:none}
.f-rule{left:68px;top:1166px;width:552px;border-top:1px solid #3c3e3c}
.copy{left:0;top:1180px;width:688px;text-align:center;font-size:6.3px;color:#888}
</style>
</head>
<body>
<div class="abs topbar"></div>
<header class="abs header"></header>
<div class="abs brand"><span class="brand-dot"></span>Fundquay</div>
<span class="abs nav" style="left:212px">How it works</span>
<span class="abs nav-sep" style="left:280px"></span>
<span class="abs nav active" style="left:291px">FAQs</span>
<span class="abs nav-sep" style="left:320px"></span>
<span class="abs nav" style="left:331px">Support</span>
<span class="abs nav-sep" style="left:372px"></span>
<span class="abs nav" style="left:380px">About</span>
<a class="abs btn btn-red" style="left:526px;top:18px;width:46px;height:18px">Register</a>
<a class="abs btn btn-dark" style="left:576px;top:18px;width:38px;height:18px">Login</a>

<h1 class="abs fund-title">Default Page Fund Title</h1>
<p class="abs fund-by">by Jonh Doe</p>

<!-- Main fund card -->
<section class="abs card" style="left:74px;top:122px;width:357px;height:333px"></section>
<div class="abs media" style="left:92px;top:140px;width:321px;height:240px">
  <div class="media-fill" role="img" aria-label="Fund video still: a man being interviewed in front of a camera" style="background:linear-gradient(120deg,#4a5560,#2c3140 55%,#4a4d68)"></div>
</div>
<svg class="abs" style="left:229px;top:239px" width="46" height="46" viewBox="0 0 46 46">
  <circle cx="23" cy="23" r="20" fill="none" stroke="#fff" stroke-width="3"/>
  <path d="M18 14 L32 23 L18 32 Z" fill="#fff"/>
</svg>
<div class="abs card-grey" style="left:74px;top:398px;width:357px;height:57px;border-top:none"></div>
<svg class="abs" style="left:92px;top:405px" width="42" height="42" viewBox="0 0 42 42">
  <circle cx="21" cy="21" r="18" fill="#fff" stroke="#d6d6d6" stroke-width="4"/>
  <path d="M21 3 A18 18 0 0 1 21 39" fill="none" stroke="var(--red)" stroke-width="4"/>
  <text x="21" y="24" text-anchor="middle" font-family="Titillium Web, sans-serif" font-size="8" font-weight="700" fill="#333">50%</text>
</svg>
<span class="abs stat-label" style="left:156px;top:414px">SUPPORTERS</span>
<span class="abs stat-value" style="left:170px;top:424px">270</span>
<span class="abs stat-sep" style="left:210px"></span>
<span class="abs stat-label" style="left:226px;top:414px">DONATIONS</span>
<span class="abs stat-value" style="left:226px;top:424px">$38,000</span>
<span class="abs stat-sep" style="left:278px"></span>
<span class="abs stat-label" style="left:295px;top:414px">VIEWS</span>
<span class="abs stat-value" style="left:300px;top:424px">25</span>
<span class="abs stat-sep" style="left:330px"></span>
<span class="abs stat-label" style="left:348px;top:414px">SHARES</span>
<span class="abs stat-value" style="left:352px;top:424px">25</span>

<!-- Tabs -->
<div class="abs tab active" style="left:74px;width:42px;height:21px">Story</div>
<div class="abs tab" style="left:122px;width:46px">Updates (12)</div>
<div class="abs tab" style="left:172px;width:52px">Comments (2)</div>

<article class="abs card" style="left:74px;top:488px;width:357px;height:560px"></article>
<h2 class="abs story-h" style="font-weight:400">LYK and Bear #1: No Food Deed Unpunished</h2>
<p class="abs story-by">by Ray Dellow in New York, NY</p>
<p class="abs para" style="top:544px">Nam sit amet est sapien, a faucibus purus. Sed commodo facilisis tempus. Pellentesque placerat elementum adipiscing. Lorem ipsum dolor sit amet, consectetuer adipiscing elit. Aenean commodo ligula eget dolor. Aenean massa. Cum sociis natoque penatibus et magnis dis parturient montes, nascetur ridiculus mus. Donec quam felis, ultricies nec, pellentesque eu, pretium quis, sem. Nulla consequat massa quis enim. Donec pede justo, fringilla vel, aliquet nec, vulputate eget, arcu.</p>
<p class="abs para" style="top:616px">Lorem ipsum dolor sit amet, consectetuer adipiscing elit. Aenean commodo ligula eget dolor. Aenean massa. Cum sociis natoque penatibus et magnis dis parturient montes, nascetur ridiculus mus. Donec quam felis, ultricies nec, pellentesque eu, pretium quis, sem. Nulla consequat massa quis enim. Donec pede justo, fringilla vel, aliquet nec, vulputate eget, arcu.</p>
<div class="abs media" style="left:91px;top:686px;width:322px;height:151px">
  <div class="media-fill" role="img" aria-label="Story photo: project friends at a meeting" style="background:linear-gradient(100deg,#8a6a52,#c29b7e 40%,#3a2e2c)"></div>
</div>
<p class="abs caption">Me and project friends on meeting</p>
<p class="abs para" style="top:870px">Nam sit amet est sapien, a faucibus purus. Sed commodo facilisis tempus. Pellentesque placerat elementum adipiscing. Lorem ipsum dolor sit amet, consectetuer adipiscing elit. Aenean commodo ligula eget dolor. Aenean massa. Cum sociis natoque penatibus et magnis dis parturient montes, nascetur ridiculus mus. Donec quam felis, ultricies nec, pellentesque eu, pretium quis, sem. Nulla consequat massa quis enim. Donec pede justo, fringilla vel, aliquet nec, vulputate eget, arcu.</p>
<div class="abs share" style="left:92px;top:948px">
  <span class="share-btn"><span class="lbl"><i class="sq"></i>Like</span><span class="cnt">16</span></span>
  <span class="share-btn"><span class="lbl"><i class="sq q"></i>Tweet</span><span class="cnt">166</span></span>
  <span class="share-btn"><span class="lbl"><i class="sq o"></i>+1</span><span class="cnt">17</span></span>
</div>
<div class="abs card-grey" style="left:74px;top:985px;width:357px;height:63px;border-top:1px solid var(--line)"></div>
<a class="abs btn btn-red" style="left:94px;top:1002px;width:75px;height:23px">Ask a question</a>
<a class="abs btn btn-dark" style="left:179px;top:1002px;width:89px;height:23px">Report this Fund</a>

<!-- Sidebar: progress -->
<aside class="abs card-grey" style="left:441px;top:122px;width:173px;height:148px"></aside>
<p class="abs side-small" style="left:453px;top:138px">Current Amount: $99,999</p>
<p class="abs side-small" style="left:453px;top:153px">Goal: $999,9999</p>
<a class="abs donate"><b>Donate on This Project</b><span>$1 minimum pledge</span></a>
<div class="abs share" style="left:451px;top:250px">
  <span class="share-btn"><span class="lbl"><i class="sq"></i>Like</span><span class="cnt">16</span></span>
  <span class="share-btn"><span class="lbl"><i class="sq q"></i>Tweet</span><span class="cnt">166</span></span>
  <span class="share-btn" style="margin-left:6px"><span class="lbl"><i class="sq o"></i>+1</span><span class="cnt">17</span></span>
</div>

<!-- Sidebar: creator -->
<aside class="abs card-grey" style="left:441px;top:288px;width:173px;height:132px"></aside>
<h3 class="abs side-title" style="left:453px;top:299px">FUND CREATED BY</h3>
<div class="abs media" style="left:453px;top:319px;width:57px;height:56px">
  <div class="media-fill" role="img" aria-label="Profile photo of Jenna Sue" style="background:linear-gradient(135deg,#8a5a3a,#c89a80)"></div>
</div>
<p class="abs side-small" style="left:522px;top:325px">Jenna Sue</p>
<p class="abs side-small" style="left:522px;top:342px">Chicago, IL</p>
<p class="abs" style="left:522px;top:354px;font-size:6.5px;color:var(--muted)">55 friends</p>
<a class="abs btn btn-red" style="left:453px;top:387px;width:57px;height:19px;font-weight:600;font-size:7px">Contact me</a>

<!-- Sidebar: recent donations -->
<aside class="abs card-grey" style="left:441px;top:438px;width:173px;height:399px"></aside>
<h3 class="abs recent-title" style="font-weight:400">RECENT DONATIONS</h3>
<div class="abs divider" style="top:481px"></div>

<span class="abs don-amount" style="top:490px">$450</span>
<span class="abs don-time" style="top:495px">5 minutes ago</span>
<div class="abs avatar photo" style="top:515px" role="img" aria-label="Donor photo"></div>
<span class="abs don-name" style="top:511px">John Doe</span>
<p class="abs don-msg" style="top:526px">Lorem ipsum dolor sit amet, consectetur adipisicing elit, sed do</p>
<div class="abs divider" style="top:565px"></div>

<span class="abs don-amount" style="top:577px">$450</span>
<span class="abs don-time" style="top:582px">5 minutes ago</span>
<div class="abs avatar" style="top:602px"></div>
<svg class="abs" style="left:462px;top:611px" width="14" height="14" viewBox="0 0 14 14"><circle cx="7" cy="4.5" r="3" fill="none" stroke="#ddd"/><path d="M1.5 13c0-3 2.5-5 5.5-5s5.5 2 5.5 5z" fill="none" stroke="#ddd"/></svg>
<span class="abs don-name" style="top:598px">John Doe</span>
<p class="abs don-msg" style="top:613px">Lorem ipsum dolor sit amet, consectetur adipisicing elit, sed do</p>
<div class="abs divider" style="top:652px"></div>

<span class="abs don-amount" style="top:666px">$450</span>
<span class="abs don-time" style="top:671px">5 minutes ago</span>
<div class="abs avatar photo" style="top:691px" role="img" aria-label="Donor photo"></div>
<span class="abs don-name" style="top:687px">John Doe</span>
<p class="abs don-msg" style="top:702px">Lorem ipsum dolor sit amet, consectetur adipisicing elit, sed do</p>
<div class="abs divider" style="top:740px"></div>

<span class="abs don-amount" style="top:753px">$450</span>
<span class="abs don-time" style="top:758px">5 minutes ago</span>
<div class="abs avatar" style="top:778px"></div>
<svg class="abs" style="left:462px;top:787px" width="14" height="14" viewBox="0 0 14 14"><circle cx="7" cy="4.5" r="3" fill="none" stroke="#ddd"/><path d="M1.5 13c0-3 2.5-5 5.5-5s5.5 2 5.5 5z" fill="none" stroke="#ddd"/></svg>
<span class="abs don-name" style="top:774px">John Doe</span>
<p class="abs don-msg" style="top:789px">Lorem ipsum dolor sit amet, consectetur adipisicing elit, sed do</p>

<!-- Footer -->
<footer class="abs footer"></footer>
<h4 class="abs f-head" style="left:76px;font-weight:400">About Us</h4>
<ul class="abs f-links" style="left:76px"><li>About Fundquay</li><li>Press Releases</li><li>Contact Us</li></ul>
<h4 class="abs f-head" style="left:239px;font-weight:400">Why Fundquay?</h4>
<ul class="abs f-links" style="left:239px"><li>Fun In Fundraising</li><li>Features</li><li>Testimonials</li><li>FAQs</li></ul>
<h4 class="abs f-head" style="left:402px;font-weight:400">Sign Up</h4>
<ul class="abs f-links" style="left:402px"><li>For a Friend/Family</li><li>For Me</li></ul>
<h4 class="abs f-head" style="left:566px;font-weight:400">Legal</h4>
<ul class="abs f-links" style="left:566px"><li>Privacy Policy</li><li>Terms &amp; Conditions</li></ul>
<div class="abs f-rule"></div>
<p class="abs copy">© 2014 Brightmoor LLC. All rights reserved.</p>
</body>
</html>
```